GLS biz card

We need a business card design for our new company based in Los Angeles called "Gold Lantern Studios". We develop film and television projects. We work with investors, financiers, film production companies, film distribution and sales companies as well as studios. We would like to incorporate our logo (see attached) on a two-sided card. We need to include: name and title, address, phone, email and company website.

Target Market(s)

Business, financial and studio clients

Industry/Entity Type

Business

Contact Information for Business Card

Two-sided. We are thinking of the logo on one side and the information on the back. Please feel free to be creative! Thanks.

Requirements
Must have
• Please include the following text information, excluding the "CAPS CATEGORY:" and please allow the ability for us to change the name, title and email address for each company employee):
• NAME & TITLE:
• Peter Dunmore
• Managing Partner
• COMPANY NAME:
• GOLD LANTERN STUDIOS (please use existing logo)
• COMPANY ADDRESS:
• KVT Arts Park
• 2480 Wexley Boulevard
• Arts Hall, 4th Floor
• Manhattan Beach, CA 90266
• COMPANY PHONE NUMBER:
• 310-555-4206
• COMPANY WEBSITE ADDRESS:
• www.goldlanternstudioshouse.com
• EMAIL ADDRESS: (only one per card)
• frank@goldlanternstudioshouse.com
• tizzy@goldlanternstudioshouse.com
• peter@goldlanternstudioshouse.com

```html
<!DOCTYPE html>
<html lang="en">
<head>
<meta charset="utf-8">
<title>Gold Lantern Studios – Business Card</title>
<link rel="stylesheet" href="https://fonts.googleapis.com/css2?family=Lato:wght@400;700;900&display=swap">
<style>
  :root {
    --stage: #3a322e;
    --card-black: #0b0b0c;
    --card-teal: #1b4753;
    --accent-cyan: #1bb8e4;
    --brand-blue: #5cc6e6;
    --text-white: #ffffff;
    --text-soft: #d9e6ea;
    --mark-dark: #101418;
  }
  * { box-sizing: border-box; margin: 0; padding: 0; }
  html, body { width: 1200px; height: 428px; overflow: hidden; }
  body {
    background: var(--stage);
    font-family: "Lato", Arial, sans-serif;
    position: relative;
  }
  .card {
    position: absolute;
    width: 520px;
    height: 297px;
    background: var(--card-black);
    border-radius: 4px;
    overflow: hidden;
    box-shadow: 0 10px 24px rgba(0,0,0,.45);
  }
  .card--back  { left: 40px;  top: 66px; }
  .card--front { left: 640px; top: 66px; }
  .card__shape { position: absolute; inset: 0; }

  .brand { position: absolute; left: 0; right: 0; text-align: center; }
  .brand__mark {
    display: block;
    margin: 0 auto;
    border-radius: 50%;
    background: var(--mark-dark);
    border: 2px solid #26343a;
  }
  .brand__name {
    display: block;
    color: var(--brand-blue);
    font-weight: 700;
    letter-spacing: .12em;
    white-space: nowrap;
  }
  .brand__tagline {
    display: block;
    color: var(--text-white);
    font-weight: 700;
    letter-spacing: .28em;
    white-space: nowrap;
  }

  .card--back .brand { top: 16px; }
  .card--back .brand__mark { width: 76px; height: 76px; }
  .card--back .brand__name { font-size: 15px; margin-top: 10px; }
  .card--back .brand__tagline { font-size: 7px; margin-top: 4px; }

  .card--front .brand { top: 36px; }
  .card--front .brand__mark { width: 122px; height: 122px; }
  .card--front .brand__name { font-size: 24px; margin-top: 14px; }
  .card--front .brand__tagline { font-size: 10px; margin-top: 8px; }

  .person { position: absolute; left: 378px; top: 178px; color: var(--text-white); }
  .person__name { font-size: 15px; font-weight: 900; }
  .person__title { font-size: 10px; font-weight: 700; margin-top: 3px; }

  .contact { position: absolute; left: 26px; top: 214px; list-style: none; }
  .contact__item {
    display: flex; align-items: center; gap: 8px;
    color: var(--text-white); font-size: 12px; font-weight: 700;
    margin-bottom: 10px;
  }
  .contact__icon { width: 13px; height: 13px; flex: none; }

  .address {
    position: absolute; left: 150px; top: 264px;
    width: 336px; height: 44px;
    background: var(--card-teal);
    border-radius: 18px 18px 0 0;
    color: var(--text-soft);
    font-size: 12px; font-weight: 700;
    text-align: center; padding-top: 9px;
  }
</style>
</head>
<body>

<section class="card card--back" aria-label="Business card, information side">
  <svg class="card__shape" viewBox="0 0 520 297" aria-hidden="true">
    <path d="M0,0 H520 V128 Q260,205 0,150 Z" fill="var(--card-teal)"/>
    <path d="M0,150 Q260,205 520,128" fill="none" stroke="var(--accent-cyan)" stroke-width="3"/>
  </svg>
  <div class="brand">
    <span class="brand__mark"></span>
    <span class="brand__name">GOLD LANTERN STUDIOS</span>
    <span class="brand__tagline">A MEDIA ENTERTAINMENT COMPANY</span>
  </div>
  <div class="person">
    <p class="person__name">YOUR NAME</p>
    <p class="person__title">Designation</p>
  </div>
  <ul class="contact">
    <li class="contact__item">
      <svg class="contact__icon" viewBox="0 0 16 16" aria-hidden="true">
        <path d="M2 5 Q8 0 14 5 L12 7 L10 5 H6 L4 7 Z" fill="#fff"/>
        <rect x="3" y="8" width="10" height="6" rx="1" fill="#fff"/>
      </svg>
      0800 555 206
    </li>
    <li class="contact__item">
      <svg class="contact__icon" viewBox="0 0 16 16" aria-hidden="true">
        <rect x="1" y="3" width="14" height="10" rx="1" fill="#fff"/>
        <path d="M1.5 4 L8 9 L14.5 4" fill="none" stroke="#0b0b0c" stroke-width="1.3"/>
      </svg>
      peter@goldlanternstudioshouse.com
    </li>
  </ul>
  <p class="address">12 Ferncliff Lane, Marlow 4102</p>
</section>

<section class="card card--front" aria-label="Business card, logo side">
  <svg class="card__shape" viewBox="0 0 520 297" aria-hidden="true">
    <path d="M0,0 H520 V200 Q300,250 0,70 Z" fill="var(--card-teal)"/>
    <path d="M0,70 Q300,250 520,200" fill="none" stroke="var(--accent-cyan)" stroke-width="3"/>
  </svg>
  <div class="brand">
    <span class="brand__mark"></span>
    <span class="brand__name">GOLD LANTERN STUDIOS</span>
    <span class="brand__tagline">A MEDIA ENTERTAINMENT COMPANY</span>
  </div>
</section>

</body>
</html>
```